property investment and development company needs a website

we need a website that looks professional and portrays trust for people looking to us to buy their house or investors looking to invest or joint venture with us.
We are based in the west midlands in the UK.
we deal mainly with residential housing, house to flats conversions, HMO's (houses in multiple ocupancy).
we require the website as a first point of contact with potential sellers, renters and investors so links or contact details that are easy to access or see would be good.
I have had logos designed by a brisk easel member and these can be used as guidance for the colour and style of the site.
Target Market(s)
joint venture investment partners, people looking to sell their house, people looking to rent from us.
Coding
Coded - Design and coding required
Number of Pages Required
3 page
Requirements
Must have
- project a professional appearance
- visable contact details

```html
<!DOCTYPE html>
<html lang="en">
<head>
<meta charset="utf-8">
<title>Marlow Homes – Property Development &amp; Investment</title>
<link href="https://fonts.googleapis.com/css2?family=Playfair+Display:wght@400;700&family=Open+Sans:wght@400;600&display=swap" rel="stylesheet">
<style>
:root{
  --gold:#c5a46d;
  --ink:#2f2f2f;
  --text:#6b6b6b;
  --light:#f4f4f4;
  --footer:#3b3b3b;
  --footer-line:#555;
  --footer-text:#cfcfcf;
  --white:#ffffff;
}
*{box-sizing:border-box;margin:0;padding:0}
html,body{width:1200px;height:2820px;overflow:hidden}
body{font-family:"Open Sans",Arial,sans-serif;color:var(--text);background:var(--white)}

/* header */
.site-header{height:64px;display:flex;align-items:center;justify-content:space-between;padding:0 60px 0 80px;background:var(--white)}
.brand{display:flex;align-items:center;gap:12px;white-space:nowrap}
.brand-mark{width:26px;height:26px;background:var(--gold)}
.brand-name{font-family:"Open Sans",Arial,sans-serif;font-weight:600;font-size:18px;color:var(--ink);letter-spacing:1px}
.main-nav{display:flex;gap:10px}
.main-nav a{font-size:13px;color:var(--ink);text-decoration:none;letter-spacing:1px;padding:7px 18px;border:1px solid transparent;border-radius:2px}
.main-nav a.active{border-color:var(--gold);color:var(--gold)}

/* hero */
.hero{position:relative;height:668px;background:linear-gradient(180deg,#dfe6ea 0%,#eef1f3 60%,#f6f6f6 100%)}
.hero-visual{position:absolute;left:0;top:0;width:700px;height:668px;background:radial-gradient(ellipse at 45% 50%,#c9a98a 0%,#b9c3c8 45%,rgba(223,230,234,0) 75%)}
.hero-copy{position:absolute;right:80px;top:258px;text-align:right;font-family:"Playfair Display",Georgia,serif;font-weight:400;color:var(--white);font-size:30px;line-height:1.4;letter-spacing:2px;text-shadow:0 1px 3px rgba(0,0,0,.35)}
.hero-dots{position:absolute;right:80px;top:392px;display:flex;gap:8px}
.hero-dots span{width:14px;height:14px;border-radius:50%;border:2px solid var(--white)}
.hero-dots span.on{background:var(--gold);border-color:var(--gold)}

/* about */
.about{height:416px;background:var(--gold);text-align:center;color:var(--white);padding-top:86px}
.section-title{font-family:"Playfair Display",Georgia,serif;font-weight:400;font-size:28px;letter-spacing:2px}
.about .rule{width:60px;height:2px;background:var(--white);margin:14px auto 26px}
.about p{width:900px;margin:0 auto 8px;font-size:13px;line-height:1.8}
.btn-outline{display:inline-block;margin-top:26px;padding:8px 26px;border:1px solid currentColor;border-radius:18px;font-size:12px;letter-spacing:1px}

/* feature rows */
.feature{position:relative;height:480px}
.feature .copy{position:absolute;width:470px}
.feature h2{font-family:"Playfair Display",Georgia,serif;font-size:26px;color:var(--ink);letter-spacing:2px;font-weight:400}
.feature .rule{width:50px;height:2px;background:var(--gold);margin:12px 0 24px}
.feature p{font-size:13px;line-height:1.85;margin-bottom:14px}
.feature .btn-outline{color:var(--gold);margin-top:10px}
.feature .visual{position:absolute}
.invest .copy{left:120px;top:86px}
.invest .visual{left:690px;top:70px;width:400px;height:330px;background:linear-gradient(150deg,#e8422b 0%,#d7331f 45%,#c98e55 75%,#f2f2f2 100%)}
.sell{height:479px}
.sell .visual{left:110px;top:20px;width:430px;height:400px;background:linear-gradient(160deg,#f3f3f3 0%,#d74035 40%,#e8e8e8 75%,#ffffff 100%)}
.sell .copy{left:620px;top:40px}
.phone-strong{color:var(--ink);font-weight:600}
.divider{height:1px;background:#e5e5e5;margin:0 110px}

/* subscribe */
.subscribe{height:292px;background:var(--light);text-align:center;padding-top:68px}
.subscribe h2{font-family:"Playfair Display",Georgia,serif;font-size:26px;color:var(--ink);letter-spacing:2px}
.subscribe h3{font-size:14px;color:var(--ink);letter-spacing:1px;margin-top:6px;font-weight:600}
.subscribe-form{display:flex;justify-content:center;gap:20px;margin-top:36px}
.subscribe-input{width:580px;height:46px;border:1px solid #d8d8d8;background:var(--white);border-radius:23px;text-align:left;padding:14px 24px;font-size:12px;color:#aaa}
.subscribe-btn{width:180px;height:46px;border-radius:23px;background:var(--gold);color:var(--white);font-size:13px;letter-spacing:1px;line-height:46px}

/* footer */
.site-footer{height:368px;background:var(--footer);color:var(--footer-text);position:relative;padding:50px 0 0 120px;display:flex;gap:80px}
.footer-col h4{font-family:"Playfair Display",Georgia,serif;font-weight:400;color:var(--gold);font-size:15px;letter-spacing:1px;margin-bottom:8px}
.footer-col .rule{width:40px;height:1px;background:var(--gold);margin-bottom:20px}
.quick-links{width:140px}
.quick-links li{list-style:none;font-size:12px;margin-bottom:16px;display:flex;align-items:center;gap:8px}
.quick-links li::before{content:"";width:4px;height:4px;background:var(--gold)}
.contact-col{width:210px}
.contact-item{display:flex;align-items:flex-start;gap:12px;font-size:12px;line-height:1.6;margin-bottom:18px}
.contact-item svg{flex:none;margin-top:2px}
.inquiry-col{width:250px}
.field{height:26px;border:1px solid var(--footer-line);margin-bottom:8px;font-size:11px;padding:5px 10px;color:#9a9a9a}
.field.tall{height:52px}
.submit{display:inline-block;padding:5px 16px;border:1px solid var(--footer-line);font-size:10px;letter-spacing:1px}
.footer-brand{position:absolute;right:100px;top:140px}
.footer-brand .brand-name{color:var(--footer-text)}

/* bottom bar */
.bottom-bar{height:52px;background:var(--gold);display:flex;align-items:center;justify-content:space-between;padding:0 120px;color:var(--white);font-size:11px;letter-spacing:1px}
.social{display:flex;gap:10px}
.social span{width:24px;height:24px;border-radius:50%;border:1px solid var(--white)}
</style>
</head>
<body>

<header class="site-header">
  <div class="brand">
    <span class="brand-mark"></span>
    <span class="brand-name">MARLOW HOMES</span>
  </div>
  <nav class="main-nav">
    <a class="active" href="#">HOME</a>
    <a href="#">ABOUT US</a>
    <a href="#">INVEST</a>
    <a href="#">SELL</a>
    <a href="#">CONTACT US</a>
  </nav>
</header>

<section class="hero">
  <div class="hero-visual" role="img" aria-label="Photo of an open hand holding a small model house"></div>
  <h1 class="hero-copy">WE ARE A PROPERTY<br>DEVELOPMENT AND<br>INVESTMENT COMPANY</h1>
  <div class="hero-dots"><span class="on"></span><span></span><span></span><span></span></div>
</section>

<section class="about">
  <h2 class="section-title">ABOUT MARLOW HOMES</h2>
  <div class="rule"></div>
  <p>Marlow Homes is a property development and investment company based in the West Midlands, working with homeowners, landlords and partners to create quality residential homes and lasting value.</p>
  <p>We buy houses quickly and fairly, convert houses into flats and manage well-run shared homes, always with honesty, clear communication and a careful eye for detail.</p>
  <span class="btn-outline">READ MORE &rsaquo;</span>
</section>

<section class="feature invest">
  <div class="copy">
    <h2>INVEST</h2>
    <div class="rule"></div>
    <p>We have our own portfolio and we are active investors, so we know what it takes to find, fund and finish a good project for every partner.</p>
    <p>Our experience in this industry enables us to offer attractive joint venture opportunities with clear returns, regular updates and a straightforward plan from start to finish.</p>
    <span class="btn-outline">READ MORE &rsaquo;</span>
  </div>
  <div class="visual" role="img" aria-label="Illustration of a house sheltered by a red umbrella with the words Smart Property Investment"></div>
</section>

<div class="divider"></div>

<section class="feature sell">
  <div class="visual" role="img" aria-label="Illustration of a white house with a red roof and a for sale tag"></div>
  <div class="copy">
    <h2>Sell</h2>
    <div class="rule"></div>
    <p>We make selling simple with a quick, fair offer for your home, no matter its condition or your reasons for moving on, giving you the maximum realistic value.</p>
    <p>Our friendly team will guide you through each step and agree a timescale that suits you.</p>
    <p>If you would like to discuss a property you are looking to sell, then please contact us on <span class="phone-strong">01234 567890</span></p>
    <span class="btn-outline">READ MORE &rsaquo;</span>
  </div>
</section>

<section class="subscribe">
  <h2>ARE YOU INVEST OR SELLING?</h2>
  <h3>SEARCH YOUR DREAM HOME</h3>
  <div class="subscribe-form">
    <div class="subscribe-input">Your email address</div>
    <div class="subscribe-btn">SUBSCRIBE NOW</div>
  </div>
</section>

<footer class="site-footer">
  <div class="footer-col quick-links">
    <h4>QUICK LINKS</h4>
    <div class="rule"></div>
    <ul>
      <li>Home</li><li>About Us</li><li>Invest</li><li>Sell</li><li>Contact Us</li>
    </ul>
  </div>
  <div class="footer-col contact-col">
    <h4>CONTACT DETAILS</h4>
    <div class="rule"></div>
    <div class="contact-item">
      <svg width="14" height="16" viewBox="0 0 14 16"><path d="M7 0a5.5 5.5 0 0 0-5.5 5.5C1.5 10 7 16 7 16s5.5-6 5.5-10.5A5.5 5.5 0 0 0 7 0zm0 7.5a2 2 0 1 1 0-4 2 2 0 0 1 0 4z" fill="var(--gold)"/></svg>
      <span>12 Linden Road, Halesford,<br>Westshire, WR0 0AA</span>
    </div>
    <div class="contact-item">
      <svg width="14" height="14" viewBox="0 0 14 14"><path d="M3 0l2.5 3-1.5 2c1 2 2.5 3.5 4.5 4.5l2-1.5 3 2.5-1.5 3C6 13 1 8 0 1.5z" fill="var(--gold)"/></svg>
      <span>07700 900123</span>
    </div>
    <div class="contact-item">
      <svg width="14" height="14" viewBox="0 0 14 14"><path d="M3 0l2.5 3-1.5 2c1 2 2.5 3.5 4.5 4.5l2-1.5 3 2.5-1.5 3C6 13 1 8 0 1.5z" fill="var(--gold)"/></svg>
      <span>01234 567890</span>
    </div>
    <div class="contact-item">
      <svg width="16" height="12" viewBox="0 0 16 12"><rect x=".5" y=".5" width="15" height="11" fill="none" stroke="var(--gold)"/><path d="M.5.5L8 7l7.5-6.5" fill="none" stroke="var(--gold)"/></svg>
      <span>info@marlowhomes.example</span>
    </div>
  </div>
  <div class="footer-col inquiry-col">
    <h4>INQUIRY FORM</h4>
    <div class="rule"></div>
    <div class="field">Your Name</div>
    <div class="field">Your Phone</div>
    <div class="field">Your Email</div>
    <div class="field tall">Your Message</div>
    <span class="submit">SUBMIT</span>
  </div>
  <div class="brand footer-brand">
    <span class="brand-mark"></span>
    <span class="brand-name">MARLOW HOMES</span>
  </div>
</footer>

<div class="bottom-bar">
  <span>&copy; 2024 MARLOW HOMES. All Rights Reserved</span>
  <div class="social"><span></span><span></span><span></span><span></span></div>
</div>

</body>
</html>
```